Real estate website

Please find attached a rough outline of what we want for the design. This is just for placement to show what to have on the menu's as content, etc. but please make it look much more professional.
Please make the bottom footer a similar gradient to the logo
Please make the sign up now and log in buttons look better - these are just samples to show placement
Please use the correct logos for dwelloria.com.au, plotnex.com.au and roofquill.com.au
Where it has 'video embed' just leave that as is as we will replace that with a video.

```html
<!DOCTYPE html>
<html lang="en">
<head>
<meta charset="utf-8">
<title>Homevane – Sell or Rent Privately in the ACT</title>
<link rel="stylesheet" href="https://fonts.googleapis.com/css2?family=Figtree:wght@300;400;600;700;800&display=swap">
<style>
  :root {
    --green-dark: #1a6b2c;
    --green-deep: #12702f;
    --green-mid: #3f9b2a;
    --tick: #8cc63f;
    --ink: #1c1c1c;
    --red: #d8102a;
    --line: #d6d6d6;
    --white: #fff;
  }
  * { box-sizing: border-box; margin: 0; padding: 0; }
  html, body { width: 1200px; height: 833px; overflow: hidden; background: var(--white); }
  body { position: relative; font-family: "Figtree", Arial, sans-serif; color: var(--ink); }

  .site-header { position: absolute; left: 0; top: 0; width: 1200px; height: 83px; background: var(--white); box-shadow: 0 2px 6px rgba(0,0,0,.12); }
  .nav-link { position: absolute; top: 32px; font-size: 18px; font-weight: 700; color: var(--green-dark); text-decoration: none; letter-spacing: .2px; }
  .btn-signup { position: absolute; left: 665px; top: 21px; width: 183px; height: 42px; border-radius: 21px; background: linear-gradient(180deg, var(--green-mid), var(--green-deep)); color: var(--white); font-size: 16px; font-weight: 700; display: flex; align-items: center; justify-content: center; letter-spacing: .5px; box-shadow: 0 2px 4px rgba(0,0,0,.2); }
  .avatar { position: absolute; left: 972px; top: 21px; }
  .btn-login { position: absolute; left: 1029px; top: 22px; width: 113px; height: 40px; border-radius: 20px; background: var(--white); box-shadow: 0 2px 6px rgba(0,0,0,.18); color: #666; font-size: 16px; font-weight: 700; display: flex; align-items: center; justify-content: center; letter-spacing: .5px; }

  .brand-mark { position: absolute; left: 58px; top: 111px; width: 130px; height: 130px; background: var(--green-mid); }
  .brand-name { position: absolute; left: 290px; top: 150px; width: 410px; text-align: right; font-size: 88px; font-weight: 300; line-height: 1; color: #111; letter-spacing: -1px; }

  .commission-title { position: absolute; left: 300px; top: 304px; width: 400px; text-align: right; font-size: 27px; font-weight: 700; color: var(--green-dark); }
  .video-slot { position: absolute; left: 58px; top: 358px; width: 250px; height: 163px; border: 1px solid var(--line); box-shadow: 0 1px 3px rgba(0,0,0,.15); display: flex; align-items: center; justify-content: center; font-size: 15px; font-weight: 600; color: #aaa; }
  .portal { position: absolute; left: 335px; display: flex; align-items: center; }
  .portal svg { width: 37px; height: 37px; }
  .portal-name { margin-left: 28px; font-size: 30px; font-weight: 700; color: var(--ink); letter-spacing: -.5px; }

  .guide-title { position: absolute; left: 752px; top: 146px; font-size: 37px; font-weight: 800; color: #222; letter-spacing: .5px; }
  .guide-sub { position: absolute; left: 752px; top: 192px; font-size: 15px; color: #222; letter-spacing: .3px; }
  .field { position: absolute; left: 752px; width: 388px; height: 40px; border-radius: 20px; background: var(--white); box-shadow: 0 2px 6px rgba(0,0,0,.18); padding-left: 21px; display: flex; align-items: center; font-size: 13px; color: #444; letter-spacing: .3px; }
  .field .req { color: var(--red); }
  .btn-submit { position: absolute; left: 752px; top: 494px; width: 140px; height: 32px; border-radius: 16px; background: linear-gradient(180deg, var(--green-mid), var(--green-deep)); color: var(--white); font-size: 12px; font-weight: 700; display: flex; align-items: center; justify-content: center; letter-spacing: .5px; }
  .captcha-badge { position: absolute; left: 907px; top: 493px; width: 127px; height: 30px; display: flex; box-shadow: 0 1px 3px rgba(0,0,0,.25); }
  .captcha-badge .left { width: 36px; background: #f4f4f4; }
  .captcha-badge .right { flex: 1; background: #4a90e2; }

  .cta { position: absolute; left: 0; top: 592px; width: 1200px; text-align: center; font-size: 37px; font-weight: 400; color: #222; letter-spacing: 1px; }
  .cta .phone { color: var(--red); font-weight: 800; }
  .intro { position: absolute; left: 89px; top: 654px; width: 1025px; font-size: 14px; line-height: 20px; text-align: justify; color: #222; letter-spacing: .55px; }

  .service-bar { position: absolute; left: 0; top: 760px; width: 1200px; height: 73px; background: linear-gradient(180deg, #66b22e 0%, #2f8e2c 55%, var(--green-deep) 100%); }
  .service-link { position: absolute; top: 28px; transform: translateX(-50%); font-size: 15px; font-weight: 700; color: var(--white); letter-spacing: .4px; white-space: nowrap; }
</style>
</head>
<body>
  <header class="site-header">
    <a class="nav-link" style="left:58px">Sell My Property</a>
    <a class="nav-link" style="left:248px">Rent My Property</a>
    <a class="nav-link" style="left:445px">Rental Management</a>
    <div class="btn-signup">SIGN UP NOW</div>
    <svg class="avatar" width="42" height="42" viewBox="0 0 42 42" aria-label="Account">
      <circle cx="21" cy="21" r="21" fill="#c8c8c8"/>
      <circle cx="21" cy="16" r="7" fill="#fff"/>
      <path d="M8 33c2-7 8-9 13-9s11 2 13 9a18 18 0 0 1-26 0z" fill="#fff"/>
    </svg>
    <div class="btn-login">LOGIN</div>
  </header>

  <div class="brand-mark"></div>
  <div class="brand-name">Homevane</div>

  <div class="commission-title">Sell with no commission on</div>
  <div class="video-slot">EMBEDDED VIDEO</div>

  <div class="portal" style="top:358px">
    <svg viewBox="0 0 40 40"><circle cx="20" cy="20" r="17" fill="none" stroke="var(--tick)" stroke-width="3"/><path d="M11 20l7 7 17-18" fill="none" stroke="var(--tick)" stroke-width="3.5" stroke-linecap="round" stroke-linejoin="round"/></svg>
    <span class="portal-name">dwelloria.com.au</span>
  </div>
  <div class="portal" style="top:422px">
    <svg viewBox="0 0 40 40"><circle cx="20" cy="20" r="17" fill="none" stroke="var(--tick)" stroke-width="3"/><path d="M11 20l7 7 17-18" fill="none" stroke="var(--tick)" stroke-width="3.5" stroke-linecap="round" stroke-linejoin="round"/></svg>
    <span class="portal-name">plotnex.com.au</span>
  </div>
  <div class="portal" style="top:486px">
    <svg viewBox="0 0 40 40"><circle cx="20" cy="20" r="17" fill="none" stroke="var(--tick)" stroke-width="3"/><path d="M11 20l7 7 17-18" fill="none" stroke="var(--tick)" stroke-width="3.5" stroke-linecap="round" stroke-linejoin="round"/></svg>
    <span class="portal-name">roofquill.com.au</span>
  </div>

  <h2 class="guide-title">Get Your FREE Guide</h2>
  <p class="guide-sub">To Listing Privately in the ACT</p>
  <div class="field" style="top:233px">First Name<span class="req">*</span></div>
  <div class="field" style="top:298px">Last Name<span class="req">*</span></div>
  <div class="field" style="top:363px">Email<span class="req">*</span></div>
  <div class="field" style="top:428px">Phone Number<span class="req">*</span></div>
  <div class="btn-submit">SUBMIT</div>
  <div class="captcha-badge"><div class="left"></div><div class="right"></div></div>

  <p class="cta">Want to Pay Nothing Upfront? Ask us How! <span class="phone">0491570156</span></p>
  <p class="intro">Listing a house in Australia for sale or rental is costly! In the ACT, it's even worse! ACT residents are paying more to list and sell online, than in other parts of Australia. <strong>Homevane solves this problem for you.</strong> Sell or rent your own home privately in the ACT with Homevane and pay zero commission. You'll be listed for an unlimited time on all the major sites. All the tools for listing are inside your account, sign up today and get started.</p>

  <nav class="service-bar">
    <span class="service-link" style="left:127px">FINANCE</span>
    <span class="service-link" style="left:278px">CONVEYANCING</span>
    <span class="service-link" style="left:481px">BUILDING INSPECTION</span>
    <span class="service-link" style="left:690px">PEST INSPECTION</span>
    <span class="service-link" style="left:853px">VALUATION</span>
    <span class="service-link" style="left:1028px">MARKET APPRAISAL</span>
  </nav>
</body>
</html>
```